Letterhead Design Project

Looking for letterhead designs for Brastova Mining.

I am looking for a letterhead design in conjunction with a business card design. I have opened contests for both but ask that if you submit a letterhead design you also submit a business card design with a corresponding look/feel.

Brastova Mining is a B2B company that buys and sells large machinery tires within the coal mining industry. The design should the strong, crisp and masculine. I have uploaded the company logo and mock-up of the back of the company's business card.

Color scheme should be grey/green/black

Contact information to include:
Name: Dale Whitford
Title: Managing Director
Phone: 555-231-4097
Address: 1817 Pellam #3 Dallas, TX 75290
Email: Dale@Brastova.example
Updates

Project Deadline Extended
Reason: Looking for a more refined, elegant letterhead than what's been submitted as of yet. Here is a sample of what we're looking for: http://www.plumcrestgallery.example/letterhead-designs/ We will also be increasing the payment.

Industry/Entity Type

Coal Mining

```html
<!DOCTYPE html>
<html lang="en">
<head>
<meta charset="utf-8">
<title>Brastova Mining – Letterhead</title>
<link rel="stylesheet" href="https://fonts.googleapis.com/css2?family=Questrial&display=swap">
<style>
  :root {
    --backdrop: #ececec;
    --paper: #f7f7f7;
    --brand-green: #4f9e1c;
    --brand-grey: #58595b;
    --ink: #4a4a4a;
    --ink-light: #ffffff;
  }
  html, body {
    margin: 0;
    padding: 0;
    width: 1200px;
    height: 936px;
    overflow: hidden;
    background: var(--backdrop);
    font-family: "Questrial", "Century Gothic", sans-serif;
  }
  .letterhead {
    position: absolute;
    left: 290px;
    top: 30px;
    width: 620px;
    height: 876px;
    background: var(--paper);
    box-shadow: 0 2px 10px rgba(0, 0, 0, 0.12);
    overflow: hidden;
  }
  .sender-band {
    position: absolute;
    left: 0;
    top: 0;
    width: 226px;
    height: 92px;
    background: var(--brand-green);
    clip-path: polygon(0 0, 100% 0, 93% 100%, 0 100%);
  }
  .sender {
    position: absolute;
    left: 40px;
    top: 34px;
    padding-left: 12px;
    border-left: 1px solid rgba(255, 255, 255, 0.7);
    color: var(--ink-light);
  }
  .sender-name {
    margin: 0;
    font-size: 13px;
    font-weight: 700;
    letter-spacing: 0.2px;
  }
  .sender-title {
    margin: 2px 0 0;
    font-size: 9px;
    opacity: 0.9;
  }
  .brand-band {
    position: absolute;
    left: 222px;
    top: 0;
    width: 262px;
    height: 64px;
    background: var(--brand-grey);
    clip-path: polygon(3% 0, 100% 0, 100% 100%, 0 100%);
    display: flex;
    align-items: center;
    padding-left: 36px;
    box-sizing: border-box;
    gap: 10px;
  }
  .brand-square {
    width: 12px;
    height: 12px;
    background: var(--brand-green);
  }
  .brand-name {
    color: var(--ink-light);
    font-size: 19px;
    letter-spacing: 2.5px;
    text-transform: uppercase;
  }
  .contact {
    position: absolute;
    right: 40px;
    bottom: 150px;
    text-align: right;
    font-size: 9px;
    line-height: 1.5;
    color: var(--ink);
  }
  .contact p { margin: 0; }
  .contact-label { color: var(--brand-green); }
</style>
</head>
<body>
  <main class="letterhead">
    <header>
      <div class="sender-band">
        <div class="sender">
          <p class="sender-name">Dale Whitford</p>
          <p class="sender-title">Managing Director</p>
        </div>
      </div>
      <div class="brand-band">
        <span class="brand-square"></span>
        <span class="brand-name">Brastova Mining</span>
      </div>
    </header>
    <footer class="contact">
      <p>1817 Pellam #3, Dallas, TX 75290</p>
      <p><span class="contact-label">Phone:</span> 555-231-4097 · <span class="contact-label">Email:</span> Dale@Brastova.example</p>
    </footer>
  </main>
</body>
</html>
```